Wellness, weight management medical practice

We have a logo but want help designing and finalizing the business card. Japanese name. Will eventually be a holistic, full-service weight management and wellness center. Will be a virtual only practice to start.

```html
<!DOCTYPE html>
<html lang="en">
<head>
<meta charset="utf-8">
<title>Alderpine Health – Business Card</title>
<link rel="stylesheet" href="https://fonts.googleapis.com/css2?family=Crimson+Pro:wght@400;600&display=swap">
<style>
  :root {
    --backdrop: #e8e5e0;
    --card-white: #ffffff;
    --marble-light: #f3f5f7;
    --marble-mid: #dde2e7;
    --marble-deep: #c9d0d7;
    --gold: #b8913f;
    --gold-soft: #c9a65a;
    --shadow: rgba(40, 30, 20, 0.35);
  }
  html, body {
    margin: 0;
    padding: 0;
    width: 900px;
    height: 1200px;
    overflow: hidden;
    background: var(--backdrop);
  }
  .canvas {
    position: relative;
    width: 900px;
    height: 1200px;
    font-family: "Crimson Pro", Georgia, serif;
    color: var(--gold);
  }
  .card {
    position: absolute;
    left: 81px;
    width: 736px;
    height: 427px;
    border-radius: 22px;
    overflow: hidden;
    box-shadow: 0 6px 14px var(--shadow);
  }
  .card--front { top: 126px; }
  .card--back { top: 637px; }

  .marble {
    position: absolute;
    inset: 0;
    background:
      radial-gradient(ellipse 260px 200px at 46% 52%, var(--card-white) 0%, rgba(255,255,255,0) 100%),
      linear-gradient(155deg, var(--marble-light) 0%, var(--marble-mid) 28%, var(--marble-light) 50%, var(--marble-deep) 72%, var(--marble-light) 100%);
  }

  /* Wordmark */
  .brand {
    position: absolute;
    display: flex;
    align-items: center;
    gap: 14px;
    white-space: nowrap;
  }
  .brand__dot {
    width: 14px;
    height: 14px;
    border-radius: 50%;
    background: var(--gold);
    flex: none;
  }
  .brand__name {
    font-weight: 400;
    color: var(--gold);
    letter-spacing: 0.06em;
  }
  .card--front .brand {
    left: 50%;
    top: 50%;
    transform: translate(-50%, -50%);
  }
  .card--front .brand__name { font-size: 40px; }

  /* Back */
  .panel {
    position: absolute;
    left: 45px;
    top: 39px;
    width: 646px;
    height: 351px;
    background: var(--card-white);
    border-radius: 20px;
  }
  .card--back .brand {
    left: 52px;
    top: 154px;
  }
  .card--back .brand__name { font-size: 27px; }
  .card--back .brand__dot { width: 11px; height: 11px; }

  .divider {
    position: absolute;
    left: 321px;
    top: 86px;
    width: 1.5px;
    height: 180px;
    background: var(--gold);
  }
  .contact {
    position: absolute;
    left: 346px;
    top: 120px;
  }
  .contact__name {
    margin: 0;
    font-size: 23px;
    font-weight: 600;
    letter-spacing: 0.08em;
    line-height: 1;
  }
  .contact__title {
    margin: 5px 0 0;
    font-size: 16px;
    letter-spacing: 0.06em;
    line-height: 1;
  }
  .contact__rule {
    width: 16px;
    height: 1px;
    background: var(--gold-soft);
    margin: 10px 0 8px;
  }
  .contact__line {
    display: flex;
    align-items: center;
    gap: 8px;
    margin: 0 0 3px;
    font-size: 16.5px;
    line-height: 18px;
    letter-spacing: 0.03em;
  }
  .contact__icon { width: 11px; height: 11px; fill: var(--gold); flex: none; }
  .address {
    position: absolute;
    left: 0;
    right: 0;
    top: 310px;
    margin: 0;
    text-align: center;
    font-size: 16.5px;
    letter-spacing: 0.04em;
  }
</style>
</head>
<body>
<main class="canvas">

  <section class="card card--front" aria-label="Business card front">
    <div class="marble" role="img" aria-label="White and grey marble texture with fine gold veins"></div>
    <div class="brand">
      <span class="brand__dot"></span>
      <span class="brand__name">Alderpine Health</span>
    </div>
  </section>

  <section class="card card--back" aria-label="Business card back">
    <div class="marble" role="img" aria-label="White and grey marble texture with fine gold veins"></div>
    <div class="panel">
      <div class="brand">
        <span class="brand__dot"></span>
        <span class="brand__name">Alderpine Health</span>
      </div>
      <div class="divider"></div>
      <div class="contact">
        <p class="contact__name">DANIEL HART</p>
        <p class="contact__title">CEO/FOUNDER</p>
        <div class="contact__rule"></div>
        <p class="contact__line">
          <svg class="contact__icon" viewBox="0 0 24 24" aria-hidden="true"><path d="M6.6 10.8a15.1 15.1 0 0 0 6.6 6.6l2.2-2.2c.3-.3.7-.4 1-.2 1.1.4 2.3.6 3.6.6.6 0 1 .4 1 1V20c0 .6-.4 1-1 1A17 17 0 0 1 3 4c0-.6.4-1 1-1h3.5c.6 0 1 .4 1 1 0 1.3.2 2.5.6 3.6.1.3 0 .7-.2 1z"/></svg>
          555-014-2287
        </p>
        <p class="contact__line">
          <svg class="contact__icon" viewBox="0 0 24 24" aria-hidden="true"><path d="M2 5h20v14H2z"/><path d="M2 6l10 7.5L22 6" fill="none" stroke="#fff" stroke-width="1.6"/></svg>
          daniel@alderpinemail.com
        </p>
      </div>
      <p class="address">118 Willow Creek Road, Suite 210, Fairhaven, MI 49410</p>
    </div>
  </section>

</main>
</body>
</html>
```